Haldor Snekker AS
Buiness cards for haldor snekker as
Haldor Snekker AS - Construction
Creative Brief
Simple
Tobias Kranveldt
CEO
Lerkeskogveien 14 0587 OSLO Norway
post@haldorsnekker.example
www.haldorsnekker.example
Org. nr.: 836 402 517
Its for a company that expanse fast within big building sites
come up with something!?! we make your investment possible

```html
<!DOCTYPE html>
<html lang="no">
<head>
<meta charset="utf-8">
<title>Haldor Snekker AS – Business Cards</title>
<link rel="stylesheet" href="https://fonts.googleapis.com/css2?family=Lora:wght@400;700&display=swap">
<style>
  :root {
    --bg: #e9ebec;
    --card-white: #ffffff;
    --card-black: #1c1c1c;
    --brand-red: #d72b22;
    --ink: #333333;
    --ink-soft: #6b6b6b;
    --shadow: rgba(0, 0, 0, 0.18);
  }
  * { box-sizing: border-box; margin: 0; padding: 0; }
  html, body {
    width: 1200px; height: 998px; overflow: hidden;
    background: var(--bg);
    font-family: "Lora", Georgia, serif;
  }
  .stage {
    position: relative; width: 1200px; height: 998px;
    display: flex; flex-direction: column; align-items: center; justify-content: center; gap: 44px;
  }
  .card {
    position: relative; width: 760px; height: 434px; overflow: hidden;
    box-shadow: 0 10px 30px var(--shadow);
  }

  /* Back side */
  .card-back { background: var(--card-black); }
  .card-back .mark {
    position: absolute; left: 50%; top: 44%; transform: translate(-50%, -50%);
    display: flex; align-items: center; gap: 16px;
  }
  .mark-square { width: 46px; height: 46px; background: var(--brand-red); }
  .card-back .mark-name { color: #ffffff; font-weight: 700; font-size: 26px; letter-spacing: 1px; }
  .card-back .web {
    position: absolute; left: 0; right: 0; bottom: 60px; text-align: center;
    color: #8a8a8a; font-size: 13px; letter-spacing: 3px;
  }

  /* Front side */
  .card-front { background: var(--card-white); }
  .card-front .mark {
    position: absolute; left: 54px; top: 168px;
    display: flex; align-items: center; gap: 14px;
  }
  .card-front .mark-square { width: 52px; height: 52px; }
  .card-front .mark-name { color: var(--ink); font-weight: 700; font-size: 24px; letter-spacing: 0.5px; }

  .divider {
    position: absolute; left: 398px; top: 52px; width: 1px; height: 250px; background: #dddddd;
  }
  .contact { position: absolute; left: 424px; top: 54px; width: 280px; color: var(--ink); }
  .contact .person { color: var(--brand-red); font-weight: 700; font-size: 24px; line-height: 1.2; }
  .contact .role { font-size: 13px; color: var(--ink-soft); margin-top: 4px; letter-spacing: 1px; }
  .contact .details { margin-top: 16px; font-size: 13px; line-height: 1.6; color: var(--ink-soft); }
  .contact .lines { margin-top: 16px; list-style: none; font-size: 13px; color: var(--ink-soft); }
  .contact .lines li { display: flex; align-items: center; gap: 10px; line-height: 1.9; }
  .contact .lines svg { width: 13px; height: 13px; flex: none; }

  .footer-band {
    position: absolute; left: 0; bottom: 34px; width: 560px; height: 32px;
    background: var(--brand-red); display: flex; align-items: center; padding-left: 54px;
  }
  .footer-band .web { color: #ffffff; font-size: 13px; letter-spacing: 3px; }
  .footer-line { position: absolute; left: 0; right: 0; bottom: 34px; height: 3px; background: var(--brand-red); }
  .edge-stripes { position: absolute; right: 0; top: 0; width: 760px; height: 434px; }
</style>
</head>
<body>
  <main class="stage">
    <section class="card card-back" aria-label="Business card, back side">
      <div class="mark">
        <span class="mark-square"></span>
        <span class="mark-name">Haldor Snekker AS</span>
      </div>
      <p class="web">www.haldorsnekker.example</p>
    </section>

    <section class="card card-front" aria-label="Business card, front side">
      <svg class="edge-stripes" viewBox="0 0 760 434" aria-hidden="true">
        <polygon points="690,196 760,196 760,226 660,226" fill="#1c1c1c"/>
        <polygon points="705,232 760,232 760,246 695,246" fill="#d72b22"/>
      </svg>

      <div class="mark">
        <span class="mark-square"></span>
        <span class="mark-name">Haldor Snekker AS</span>
      </div>

      <span class="divider"></span>

      <div class="contact">
        <p class="person">Tobias Kranveldt</p>
        <p class="role">CEO</p>
        <p class="details">
          Org. nr.: 836 402 517<br>
          Lerkeskogveien 14<br>
          0587 OSLO - Norway
        </p>
        <ul class="lines">
          <li>
            <svg viewBox="0 0 14 14"><rect x="3" y="0.5" width="8" height="13" rx="1.5" fill="#d72b22"/><rect x="4.5" y="2" width="5" height="8" fill="#fff"/></svg>
            +47 482 19 306
          </li>
          <li>
            <svg viewBox="0 0 14 14"><path d="M3 1 L5.5 1 L6.5 4 L5 5.2 Q6.5 8.5 8.8 9 L10 7.5 L13 8.5 L13 11 Q12 13 9.5 12.5 Q2 10.5 1.5 3.5 Q1.5 1.5 3 1 Z" fill="#d72b22"/></svg>
            +47 23 18 77 20
          </li>
          <li>
            <svg viewBox="0 0 14 14"><rect x="0.5" y="2.5" width="13" height="9" fill="#d72b22"/><polyline points="0.5,2.5 7,8 13.5,2.5" fill="none" stroke="#fff" stroke-width="1.2"/></svg>
            post@haldorsnekker.example
          </li>
        </ul>
      </div>

      <div class="footer-line"></div>
      <div class="footer-band"><span class="web">www.haldorsnekker.example</span></div>
    </section>
  </main>
</body>
</html>
```